CREATIVE, BEAUTIFUL, STANDOUT BUSINESS CARD WITH LOGO DESIRED

Hello. I am a screenwriter, going to Hollywood soon to seek representation by agents and managers, as well as to pitch my screenplays and TV scripts to producers.

I need a CREATIVE, BEAUTIFUL, STANDOUT ONE-SIDED business card and LOGO with the following features:

Marcus Pell
Screenwriter
--- This part ("Marcus Pell" on one line, and "Screenwriter" on the next) should be an enticing logo, for which I need a separate file, so that I can also use it for branding on my website, social media, etc.
Then, as part of the same text set, under my name and profession should be my contact information:
Phone: 555 - 214 - 7386
Email: marcuspell@[login to view URL]
Website: [login to view URL]

The second text set should contain the following:

LOGLINE: A brilliant, shrewd Hollywood visionary joins forces with a talented, prolific screenwriter to create wonderful stories and make lots of money together. Make this your story at www.marcuspellwrites.com.

With this message, I am uploading two attachments:

1. My photo
2. The text sets the card should contain.

You can use your design flair and creativity to work with layout, colors and design.

It should be dynamic and, when the recipient of the business card is sifting through the 60 or so cards they received that day, it should stand out and help them remember me, and make them want to reach out.

By entering this contest, you agree that, if you win, I will receive the source file for the business card, and the source file for the logo, so that I can make future changes, as well as the rights to them, so I can use the logo on my website, social media, advertising, etc.

Feel free to ask questions.

Thank you for your help, and good luck to you!

Marcus

```html
<!DOCTYPE html>
<html lang="en">
<head>
<meta charset="utf-8">
<title>Marcus Pell – Screenwriter Business Card</title>
<link rel="stylesheet" href="https://fonts.googleapis.com/css2?family=Lato:wght@300;400;700&display=swap">
<style>
  :root {
    --page: #ffffff;
    --card: #25272a;
    --band-dark: #151617;
    --blue: #0b30d0;
    --blue-shade: #0a2399;
    --navy: #0d2a8a;
    --divider: #f4eef1;
    --seal-fill: #eef2fb;
    --ink-light: #f3e9ee;
    --ink-soft: #b9bdc8;
    --accent: #5d7bff;
    --seal-ink: #0d2a8a;
  }
  html, body {
    margin: 0;
    padding: 0;
    width: 1200px;
    height: 763px;
    overflow: hidden;
    background: var(--page);
  }
  .canvas {
    position: relative;
    width: 1200px;
    height: 763px;
    font-family: "Lato", sans-serif;
  }
  .card-art {
    position: absolute;
    inset: 0;
  }
  .card-name {
    position: absolute;
    left: 564px;
    top: 404px;
    transform: translateX(-50%);
    margin: 0;
    font-weight: 400;
    font-size: 48px;
    letter-spacing: 0.12em;
    color: var(--ink-light);
    white-space: nowrap;
    line-height: 1;
  }
  .card-role {
    position: absolute;
    left: 549px;
    top: 475px;
    transform: translateX(-50%);
    margin: 0;
    font-weight: 400;
    font-size: 20px;
    letter-spacing: 0.32em;
    color: var(--ink-light);
    white-space: nowrap;
    line-height: 1;
  }
  .contact-list {
    position: absolute;
    left: 551px;
    top: 530px;
    transform: translateX(-50%);
    margin: 0;
    padding: 0;
    list-style: none;
    display: flex;
    gap: 26px;
    font-size: 15px;
    font-weight: 400;
    color: var(--ink-light);
    white-space: nowrap;
    line-height: 1;
  }
  .contact-list__label {
    font-weight: 700;
    color: var(--accent);
    margin-right: 6px;
  }
  .logline {
    position: absolute;
    left: 181px;
    top: 568px;
    width: 740px;
    margin: 0;
    font-size: 14px;
    font-weight: 300;
    line-height: 1.55;
    color: var(--ink-soft);
    text-align: center;
  }
  .logline__label {
    font-weight: 700;
    letter-spacing: 0.12em;
    color: var(--accent);
    margin-right: 6px;
  }
  .logline__link {
    font-weight: 400;
    color: var(--ink-light);
  }
  .brand-seal {
    position: absolute;
    left: 464px;
    top: 176px;
    width: 200px;
    height: 200px;
    display: flex;
    align-items: center;
    justify-content: center;
  }
  .brand-seal__disc {
    position: absolute;
    inset: 0;
    border-radius: 50%;
    background: var(--seal-fill);
    border: 12px solid var(--navy);
    box-sizing: border-box;
  }
  .brand-seal__name {
    position: relative;
    font-weight: 700;
    font-size: 26px;
    color: var(--seal-ink);
    white-space: nowrap;
  }
</style>
</head>
<body>
<main class="canvas">
  <svg class="card-art" width="1200" height="763" viewBox="0 0 1200 763" aria-hidden="true">
    <defs>
      <clipPath id="card-shape">
        <rect x="83" y="60" width="1040" height="596" rx="22" ry="22"/>
      </clipPath>
    </defs>
    <g clip-path="url(#card-shape)">
      <rect class="card-base" x="83" y="60" width="1040" height="596" fill="var(--card)"/>
      <rect class="edge-band" x="83" y="60" width="54" height="596" fill="var(--blue)"/>
      <rect class="name-rail-shadow" x="137" y="455" width="828" height="49" fill="var(--band-dark)"/>
      <rect class="name-rail" x="137" y="425" width="151" height="30" fill="var(--blue)"/>
      <polygon class="rail-bevel" points="288,425 367,473 367,504 288,455" fill="var(--blue-shade)"/>
      <rect class="name-rail" x="813" y="425" width="152" height="30" fill="var(--blue)"/>
      <polygon class="rail-bevel" points="813,425 731,473 731,504 813,455" fill="var(--blue-shade)"/>
      <rect class="role-plate" x="367" y="473" width="364" height="31" fill="var(--blue)"/>
      <polyline class="divider" points="969,60 969,335 952,360 969,383 969,656" fill="none" stroke="var(--divider)" stroke-width="8"/>
      <rect class="column-top" x="977" y="60" width="84" height="267" fill="var(--navy)"/>
      <polygon class="column-bevel" points="977,327 1061,327 1061,387 977,387 963,357" fill="var(--blue-shade)"/>
      <polygon class="column-bevel-face" points="977,327 1061,327 1061,352 963,357" fill="var(--blue)"/>
      <rect class="column-bottom" x="977" y="387" width="84" height="269" fill="var(--blue)"/>
    </g>
  </svg>

  <div class="brand-seal">
    <div class="brand-seal__disc"></div>
    <span class="brand-seal__name">Marcus Pell</span>
  </div>

  <h1 class="card-name">Marcus Pell</h1>
  <p class="card-role">screenwriter</p>

  <ul class="contact-list">
    <li><span class="contact-list__label">Phone:</span>555 - 214 - 7386</li>
    <li><span class="contact-list__label">Email:</span>marcuspell@[login to view URL]</li>
    <li><span class="contact-list__label">Website:</span>www.marcuspellwrites.com</li>
  </ul>

  <p class="logline"><span class="logline__label">LOGLINE:</span>A brilliant, shrewd Hollywood visionary joins forces with a talented, prolific screenwriter to create wonderful stories and make lots of money together. Make this your story at <span class="logline__link">www.marcuspellwrites.com</span>.</p>
</main>
</body>
</html>
```